Poster of Core Values & Motto

Create our core values poster and motto. Attached are our core values and our Motto. This poster represents both of our companies Tidy Pulp & CuraBinix.

Target Market(s)

Our team / employees

Industry/Entity Type

Shredding and Medical Waste

Colors
59FF00
82FF00
B8FF75
E3FFCB
F4FFEA
EB3D1F
EC4F4E
F09395
F8D3D4
FCEDEE

Requirements
Must have
• Include both companies logos

```html
<!DOCTYPE html>
<html lang="en">
<head>
<meta charset="utf-8">
<title>Core Values and Motto Poster</title>
<link href="https://fonts.googleapis.com/css2?family=Barlow+Semi+Condensed:wght@400;500;600;700&display=swap" rel="stylesheet">
<style>
  :root {
    --red: #d71f26;
    --dark: #2b2b2b;
    --ink: #1f1f1f;
    --panel: #f2f2f2;
    --paper: #ffffff;
    --backdrop: #e9e9e9;
    --green: #2c9a3a;
    --rule: #e6e6e6;
  }
  * { box-sizing: border-box; margin: 0; padding: 0; }
  html, body { width: 1200px; height: 612px; overflow: hidden; }
  body {
    background: var(--backdrop);
    font-family: "Barlow Semi Condensed", Arial, sans-serif;
    color: var(--ink);
    position: relative;
  }
  .poster {
    position: absolute;
    left: 393px; top: 14px;
    width: 414px; height: 584px;
    background: var(--paper);
    box-shadow: 0 4px 14px rgba(0,0,0,.18);
    overflow: hidden;
  }
  .header { position: absolute; left: 0; top: 0; width: 414px; height: 90px; }
  .header svg { position: absolute; inset: 0; }
  .title {
    position: absolute; left: 0; right: 0; top: 10px;
    text-align: center; color: #fff;
    font-weight: 700; font-size: 38px; line-height: 35px; letter-spacing: .5px;
  }
  .motto {
    position: absolute; left: 0; top: 90px; width: 100%; height: 53px;
    background: var(--panel); text-align: center;
  }
  .motto-words { color: var(--red); font-weight: 700; font-size: 16px; margin-top: 7px; line-height: 18px; }
  .motto-line { font-size: 15px; font-weight: 500; line-height: 20px; }
  .values { position: absolute; left: 0; top: 143px; width: 100%; height: 396px; }
  .spine { position: absolute; left: 44px; top: 43px; width: 2px; height: 309px; background: var(--red); }
  .value { position: absolute; left: 0; width: 100%; height: 60px; }
  .value::after {
    content: ""; position: absolute; left: 70px; right: 20px; bottom: 0; height: 2px;
    background: linear-gradient(90deg, var(--rule), rgba(230,230,230,0));
  }
  .value:last-child::after { display: none; }
  .value-icon {
    position: absolute; left: 24px; top: 9px; width: 42px; height: 42px;
    border-radius: 50%; background: var(--red);
    display: flex; align-items: center; justify-content: center;
  }
  .value-icon svg { width: 22px; height: 22px; fill: none; stroke: #fff; stroke-width: 1.6; stroke-linecap: round; stroke-linejoin: round; }
  .value-name { position: absolute; left: 82px; top: 7px; font-weight: 700; font-size: 19px; line-height: 22px; }
  .value-text { position: absolute; left: 82px; top: 31px; font-size: 13px; font-weight: 500; line-height: 16px; }
  .footer {
    position: absolute; left: 0; bottom: 0; width: 100%; height: 47px;
    background: var(--panel);
    display: flex; align-items: center; justify-content: space-between; padding: 0 20px;
  }
  .brand { font-weight: 700; font-size: 18px; letter-spacing: .5px; display: flex; align-items: center; gap: 6px; }
  .brand-cura { color: var(--red); }
  .brand-tidy { color: var(--green); }
  .brand-dot { width: 10px; height: 10px; border-radius: 50%; background: var(--green); }
</style>
</head>
<body>
  <main class="poster">
    <header class="header">
      <svg viewBox="0 0 414 90" width="414" height="90">
        <rect width="414" height="90" fill="var(--red)"/>
        <polygon points="0,0 65,0 0,77" fill="var(--dark)"/>
        <polygon points="414,24 414,90 355,90" fill="var(--dark)"/>
        <line x1="68" y1="0" x2="2" y2="82" stroke="#fff" stroke-width="2"/>
        <line x1="414" y1="20" x2="350" y2="90" stroke="#fff" stroke-width="2"/>
      </svg>
      <h1 class="title">CORE VALUES<br>AND&nbsp; MOTTO</h1>
    </header>

    <section class="motto">
      <p class="motto-words">Purpose / Cause / Passion</p>
      <p class="motto-line">Remind people what great service looks like.</p>
    </section>

    <section class="values">
      <div class="spine"></div>

      <div class="value" style="top:13px">
        <div class="value-icon"><svg viewBox="0 0 24 24"><circle cx="12" cy="8" r="3"/><circle cx="6" cy="10" r="2.2"/><circle cx="18" cy="10" r="2.2"/><path d="M7 19c0-3 2.2-5 5-5s5 2 5 5z"/><path d="M2.5 17c0-2 1.5-3.5 3.5-3.5M21.5 17c0-2-1.5-3.5-3.5-3.5"/></svg></div>
        <h2 class="value-name">Synergy/Teamwork</h2>
        <p class="value-text">Get It Done Attitude with Humble confidence</p>
      </div>

      <div class="value" style="top:82px">
        <div class="value-icon"><svg viewBox="0 0 24 24"><path d="M8 2l4 7 4-7"/><circle cx="12" cy="15" r="6"/><circle cx="12" cy="15" r="3"/></svg></div>
        <h2 class="value-name">Excellence</h2>
        <p class="value-text">Exceed expectations with a smile</p>
      </div>

      <div class="value" style="top:143px">
        <div class="value-icon"><svg viewBox="0 0 24 24"><path d="M4 12a8 8 0 0 1 13-6.2M20 12a8 8 0 0 1-13 6.2"/><path d="M17 2.5v3.5h-3.5M7 21.5V18h3.5"/><path d="M13 7l-3 5.5h4L11 17"/></svg></div>
        <h2 class="value-name">Efficient</h2>
        <p class="value-text">On-Time, sense of urgency, always trying to improve</p>
      </div>

      <div class="value" style="top:202px">
        <div class="value-icon"><svg viewBox="0 0 24 24"><path d="M12 2.5l7.5 3v6c0 5-3.4 8.5-7.5 10-4.1-1.5-7.5-5-7.5-10v-6z"/><path d="M8.5 12l2.5 2.5 4.5-5"/></svg></div>
        <h2 class="value-name">Safe &amp; Secure</h2>
        <p class="value-text">We are just as secure as an armored truck with money</p>
      </div>

      <div class="value" style="top:262px">
        <div class="value-icon"><svg viewBox="0 0 24 24"><rect x="3" y="11" width="4" height="9"/><path d="M7 12l4-6c1-1 2.5-.5 2.3 1l-.6 3.5H19c1.2 0 2 1 1.7 2.2l-1.5 6c-.3 1-1 1.3-2 1.3H7"/></svg></div>
        <h2 class="value-name">Honesty/Integrity</h2>
        <p class="value-text">Do the right thing</p>
      </div>

      <div class="value" style="top:322px">
        <div class="value-icon"><svg viewBox="0 0 24 24"><circle cx="12" cy="12" r="2.5"/><circle cx="5" cy="5" r="2"/><circle cx="19" cy="5" r="2"/><circle cx="5" cy="19" r="2"/><circle cx="19" cy="19" r="2"/><path d="M6.5 6.5l3.7 3.7M17.5 6.5l-3.7 3.7M6.5 17.5l3.7-3.7M17.5 17.5l-3.7-3.7"/></svg></div>
        <h2 class="value-name">Dependable</h2>
        <p class="value-text">Do what you say you will do</p>
      </div>
    </section>

    <footer class="footer">
      <span class="brand brand-cura">CuraBinix</span>
      <span class="brand brand-tidy"><span class="brand-dot"></span>Tidy Pulp</span>
    </footer>
  </main>
</body>
</html>
```